I'm an EDM producer that needs artwork for a single cover.

I am looking for artwork for a single cover. The song is a progressive house track so it is very hard hitting and aggressive. I would like the artwork to abstract but not entirely. The song is named "Velocity", which is a chemical in the brain so I was thinking something maybe involving a brain but it doesn't have to be. I like both the cleaned up look as well as the abstract look. Maybe they can be blended in together? Like for the most part clean and an abstract design in the middle? I'm not too particular. Feel free to do what you want and be creative. I just don't want it to look relaxing because the song is the opposite. I added some album artwork that i like. The first one with the two Cs put together is one i really like. Also, I want my name "Lenny Marsoud" on the cover as well as the song title.

Target Market(s)

Millenials and other EDM fans

Industry/Entity Type

Progressive

Requirements
Should not have
• Beaches or any other calming designs

```html
<!DOCTYPE html>
<html lang="en">
<head>
<meta charset="utf-8">
<title>Lenny Marsoud – Velocity</title>
<link href="https://fonts.googleapis.com/css2?family=Comfortaa:wght@300;400;700&display=swap" rel="stylesheet">
<style>
  :root {
    --page-bg: #ffffff;
    --cover-bg: #121212;
    --artist-fill: #e9dcc0;
    --artist-stroke: #ffffff;
    --artist-glow: rgba(120, 150, 255, 0.5);
    --title-color: #c9c9c9;
    --sphere-core: #f4f7ff;
    --sphere-rim: #9fb2e8;
    --neuron-hot: #b04a9c;
    --neuron-mid: #6a4fb0;
    --neuron-edge: #2a1d45;
  }
  * { margin: 0; padding: 0; box-sizing: border-box; }
  html, body {
    width: 1200px;
    height: 1000px;
    overflow: hidden;
    background: var(--page-bg);
  }
  .canvas {
    position: relative;
    width: 1200px;
    height: 1000px;
  }
  .cover {
    position: absolute;
    left: 295px;
    top: 15px;
    width: 594px;
    height: 594px;
    background: var(--cover-bg);
    overflow: hidden;
  }
  .cover-art {
    position: absolute;
    left: 65px;
    top: 55px;
    width: 450px;
    height: 380px;
  }
  .cover-art svg { width: 100%; height: 100%; display: block; }
  .artist-name,
  .artist-name-reflection {
    position: absolute;
    left: 0;
    width: 100%;
    text-align: center;
    font-family: "Comfortaa", sans-serif;
    font-weight: 700;
    font-size: 33px;
    letter-spacing: 0.5px;
    line-height: 1;
  }
  .artist-name {
    top: 470px;
    color: var(--artist-fill);
    -webkit-text-stroke: 1px var(--artist-stroke);
    text-shadow: 0 0 6px var(--artist-glow), 0 2px 3px rgba(0,0,0,0.8);
  }
  .artist-name-reflection {
    top: 446px;
    color: rgba(200, 190, 170, 0.16);
    transform: scaleY(-1);
    filter: blur(1.5px);
  }
  .song-title {
    position: absolute;
    left: 0;
    width: 100%;
    top: 515px;
    text-align: center;
    font-family: "Comfortaa", sans-serif;
    font-weight: 300;
    font-size: 25px;
    line-height: 1;
    letter-spacing: 1px;
    color: var(--title-color);
  }
</style>
</head>
<body>
  <main class="canvas">
    <section class="cover">
      <div class="cover-art" role="img" aria-label="Abstract illustration of spiky purple neurons with long tendrils gripping a bright silver perforated sphere, with scattered glass droplets">
        <svg viewBox="0 0 450 380" aria-hidden="true">
          <defs>
            <radialGradient id="neuron-burst" cx="56%" cy="54%" r="52%">
              <stop offset="0%" stop-color="var(--sphere-core)" stop-opacity="1"/>
              <stop offset="20%" stop-color="#d6e0ff" stop-opacity="1"/>
              <stop offset="27%" stop-color="var(--sphere-rim)" stop-opacity="0.95"/>
              <stop offset="31%" stop-color="var(--neuron-hot)" stop-opacity="0.85"/>
              <stop offset="52%" stop-color="var(--neuron-mid)" stop-opacity="0.55"/>
              <stop offset="78%" stop-color="var(--neuron-edge)" stop-opacity="0.25"/>
              <stop offset="100%" stop-color="var(--neuron-edge)" stop-opacity="0"/>
            </radialGradient>
          </defs>
          <ellipse cx="225" cy="190" rx="225" ry="190" fill="url(#neuron-burst)"/>
        </svg>
      </div>
      <div class="artist-name-reflection" aria-hidden="true">lenny marsoud</div>
      <h1 class="artist-name">lenny marsoud</h1>
      <p class="song-title">[velocity]</p>
    </section>
  </main>
</body>
</html>
```